Roofing Company needs YOU to help put us on top!

Brightpeak Roofing, a fresh new company with quality and Innovation in mind, needs your help to stand out in the competitive Chicago market. With over 30 years of experience, all the right people and tools for the job, the only thing we are missing is your creative ideas in web design to help us grow our online presence.
Our Company offers exceptional quality at reasonable prices, we work for the everyday people both blue collar and white collar.

We have used Craftswarm in the past with multiple successful campaigns, we are excited to see what you can come up with for our website.

www.BrightpeakRoofing.example will be the domain

We will be hiring a photographer for visual content on our pages later. Stock photos are okay to use but should follow theme.

Thank you for taking the time on the submissions, if you have any questions don't hesitate to ask and we will provide whatever is needed to you.

Target Market(s)

Homeowners & Commercial Clients between 21-65

Industry/Entity Type

Roofing

Coding

Coded - Design and coding required

Number of Pages Required

4 page

Font styles to use
Sans Serif

Colors
ffffff
ec1f27
000000
5c5c5c
757575
b2b2b2

Requirements
Must have
• Color Scheme - should follow around our logo
• As for pages we were looking for an About, Services, Projects (gallery page) and Contact.
• Main page please include social media links and a a place so people could use tillbee to make payments
• Website should work on desktop as well as mobile platforms
Nice to have
• A Live chat feature would be nice if possible
Should not have
• Obscure Colors or Common web templates

```html
<!DOCTYPE html>
<html lang="en">
<head>
<meta charset="utf-8">
<title>Contact – Brightpeak Roofing</title>
<link href="https://fonts.googleapis.com/css2?family=Roboto:wght@400;500;700&family=Poppins:wght@400;500&display=swap" rel="stylesheet">
<style>
:root{
  --red:#ec1f27;
  --black:#000000;
  --ink:#1e1e1e;
  --grey-dark:#5c5c5c;
  --grey:#757575;
  --grey-light:#b2b2b2;
  --banner:#23262a;
  --footer-bg:#f0f1f3;
  --white:#ffffff;
  --rule:#e2e2e2;
}
*{box-sizing:border-box;margin:0;padding:0}
html,body{width:1200px;height:844px;overflow:hidden;background:var(--white)}
body{position:relative;font-family:Roboto,Arial,sans-serif;color:var(--ink)}
a{color:inherit;text-decoration:none}
.abs{position:absolute}

/* header */
.topbar{left:356px;top:0;width:844px;height:39px;background:var(--red);
  clip-path:polygon(0 0,100% 0,100% 100%,34px 100%)}
.topbar-phone{top:12px;color:var(--white);font-size:13px;font-weight:500;display:flex;align-items:center;gap:6px}
.topbar-social{top:13px;right:97px;display:flex;gap:12px}
.topbar-social span{width:12px;height:12px;border-radius:50%;background:var(--white)}
.brand{left:89px;top:22px;display:flex;align-items:center;gap:8px}
.brand-mark{width:16px;height:16px;background:var(--red)}
.brand-name{font-size:23px;font-weight:700;color:var(--black);letter-spacing:-.2px}
.nav{top:59px;font-size:12px;font-weight:500;color:var(--black)}
.nav.active{color:var(--red)}
.nav-underline{left:1023px;top:86px;width:44px;height:2px;background:var(--red)}
.search{left:1098px;top:57px}

/* banner */
.banner{left:0;top:89px;width:1200px;height:78px;background:linear-gradient(90deg,#1f2226 0%,#2a2d31 55%,#3a3d41 100%)}
.banner-title{left:90px;top:123px;color:var(--white);font-size:18px;font-weight:700}
.crumbs{right:69px;top:125px;font-size:13px;font-weight:500;display:flex;gap:14px;color:var(--white)}
.crumbs .home{color:var(--red)}

/* contact info */
.section-title{top:206px;font-family:Poppins,Arial,sans-serif;font-size:17px;color:var(--ink);text-align:center}
.divider{left:599px;top:196px;width:1px;height:360px;background:var(--rule)}
.vline{left:312px;top:251px;height:266px;border-left:1px dotted #cfcfcf}
.hline{left:92px;top:383px;width:441px;border-top:1px dotted #cfcfcf}
.info{width:220px;text-align:center}
.info svg{display:block;margin:0 auto}
.info h3{font-family:Poppins,Arial,sans-serif;font-size:10.5px;font-weight:500;letter-spacing:1.6px;color:var(--ink);margin-top:14px}
.info p{font-size:12px;line-height:18px;color:var(--grey);margin-top:12px}

/* form */
.form{left:668px;top:251px;width:445px;height:266px;border:1px solid #e4e4e4;border-radius:7px;background:var(--white);box-shadow:0 6px 14px rgba(236,31,39,.18);overflow:hidden}
.field{position:absolute;padding:12px 20px}
.field label{display:block;font-family:Poppins,Arial,sans-serif;font-size:8px;color:var(--grey-light)}
.field .val{display:block;font-size:12px;color:var(--ink);margin-top:5px}
.f-first{left:0;top:0;width:223px;height:53px;border-right:1px solid #e4e4e4;border-bottom:1px solid #e4e4e4}
.f-second{left:223px;top:0;width:222px;height:53px;border-bottom:1px solid #e4e4e4}
.f-msg{left:0;top:53px;width:445px;height:160px;padding-top:18px}
.f-msg label{font-size:11px}
.send{position:absolute;left:0;bottom:0;width:445px;height:53px;background:var(--red);color:var(--white);font-size:13px;font-weight:500;display:flex;align-items:center;justify-content:center}

/* footer */
.footer{left:0;top:594px;width:1200px;height:206px;background:var(--footer-bg)}
.fcol{top:629px}
.fcol h4{font-size:16.5px;font-weight:500;color:var(--ink);margin-bottom:14px}
.fcol p{font-size:13px;line-height:22px;color:var(--ink)}
.fcol ul{list-style:none}
.fcol li{font-size:13px;line-height:22px;color:var(--ink);padding-left:2px}
.follow li{line-height:27px;display:flex;align-items:center;gap:10px;padding-left:0}
.follow li i{width:7px;height:7px;background:var(--ink);display:inline-block}
.follow li.hot{color:var(--red)}
.follow li.hot i{background:var(--red)}
.pay{margin-top:12px;font-size:16px;font-weight:700;color:var(--grey)}
.bottombar{left:0;top:800px;width:1200px;height:44px;background:var(--red);color:var(--white);font-size:14px;font-weight:500}
.copy{left:90px;top:14px}
.legal{right:69px;top:14px;display:flex;gap:17px}
</style>
</head>
<body>

<header>
  <div class="abs topbar"></div>
  <div class="abs topbar-phone" style="left:396px">
    <svg width="12" height="12" viewBox="0 0 24 24"><path fill="#fff" d="M6.6 10.8a15.1 15.1 0 0 0 6.6 6.6l2.2-2.2c.3-.3.7-.4 1-.2 1.1.4 2.3.6 3.6.6.6 0 1 .4 1 1V20c0 .6-.4 1-1 1A17 17 0 0 1 3 4c0-.6.4-1 1-1h3.5c.6 0 1 .4 1 1 0 1.3.2 2.5.6 3.6.1.3 0 .7-.2 1z"/></svg>
    Illinois: 708-555-0142
  </div>
  <div class="abs topbar-phone" style="left:565px">
    <svg width="12" height="12" viewBox="0 0 24 24"><path fill="#fff" d="M6.6 10.8a15.1 15.1 0 0 0 6.6 6.6l2.2-2.2c.3-.3.7-.4 1-.2 1.1.4 2.3.6 3.6.6.6 0 1 .4 1 1V20c0 .6-.4 1-1 1A17 17 0 0 1 3 4c0-.6.4-1 1-1h3.5c.6 0 1 .4 1 1 0 1.3.2 2.5.6 3.6.1.3 0 .7-.2 1z"/></svg>
    Indiana: 219-555-0187
  </div>
  <div class="abs topbar-social" aria-label="Social links"><span></span><span></span><span></span><span></span></div>

  <a class="abs brand" href="#"><span class="brand-mark"></span><span class="brand-name">Brightpeak Roofing</span></a>

  <nav>
    <a class="abs nav" style="left:724px" href="#">HOME</a>
    <a class="abs nav" style="left:786px" href="#">ABOUT</a>
    <a class="abs nav" style="left:852px" href="#">SERVICES</a>
    <a class="abs nav" style="left:934px" href="#">PROJECTS</a>
    <a class="abs nav active" style="left:1020px" href="#">CONTACT</a>
    <div class="abs nav-underline"></div>
    <svg class="abs search" width="14" height="14" viewBox="0 0 24 24" fill="none" stroke="#222" stroke-width="2"><circle cx="10" cy="10" r="7"/><path d="M15 15l6 6"/></svg>
  </nav>
</header>

<section>
  <div class="abs banner" role="img" aria-label="Darkened photo of a modern building facade"></div>
  <h1 class="abs banner-title">CONTACT</h1>
  <div class="abs crumbs"><span class="home">HOME</span><span>›</span><span>CONTACT</span></div>
</section>

<main>
  <h2 class="abs section-title" style="left:203px;width:220px">Contact Info</h2>
  <div class="abs vline"></div>
  <div class="abs hline"></div>

  <div class="abs info" style="left:92px;top:250px">
    <svg width="26" height="30" viewBox="0 0 26 30" fill="none" stroke="#ec1f27" stroke-width="1.5"><path d="M13 29S2 18 2 11a11 11 0 0 1 22 0c0 7-11 18-11 18z"/><circle cx="13" cy="11" r="5"/></svg>
    <h3>ADDRESS</h3>
    <p>Some address line here,<br>with location information</p>
  </div>
  <div class="abs info" style="left:314px;top:250px">
    <svg width="30" height="30" viewBox="0 0 30 30" fill="none" stroke="#ec1f27" stroke-width="1.5"><path d="M8 3l4 6-3 3c1.5 3.5 4.5 6.5 8 8l3-3 6 4-3 5C12 26 4 18 3 7z"/><path d="M17 3a10 10 0 0 1 10 10M17 8a5 5 0 0 1 5 5"/></svg>
    <h3>PHONE</h3>
    <p>708-555-0142<br>219-555-0187</p>
  </div>
  <div class="abs info" style="left:92px;top:409px">
    <svg width="30" height="24" viewBox="0 0 30 24" fill="none" stroke="#ec1f27" stroke-width="1.5"><rect x="1.5" y="1.5" width="27" height="21"/><path d="M1.5 1.5L15 13 28.5 1.5M1.5 22.5l10-10M28.5 22.5l-10-10"/></svg>
    <h3>E-MAIL</h3>
    <p>info@brightpeakroofing.example</p>
  </div>
  <div class="abs info" style="left:314px;top:409px">
    <svg width="32" height="32" viewBox="0 0 32 32" fill="none" stroke="#ec1f27" stroke-width="1.5"><path d="M28 16A12 12 0 1 1 16 4"/><path d="M16 10v7h5"/><path d="M22 2l-3 3 3 3"/></svg>
    <h3>WORKING HOURS</h3>
    <p>Monday - Friday: 8am - 8pm<br>Saturday 9am - 1pm</p>
  </div>

  <div class="abs divider"></div>

  <h2 class="abs section-title" style="left:781px;width:220px">Write to us</h2>
  <form class="abs form">
    <div class="field f-first"><label>First Name</label><span class="val">Mark</span></div>
    <div class="field f-second"><label>Second Name</label><span class="val">Doe</span></div>
    <div class="field f-msg"><label>Message</label></div>
    <div class="send">Send Message</div>
  </form>
</main>

<footer>
  <div class="abs footer"></div>
  <div class="abs fcol" style="left:88px">
    <h4>About Us</h4>
    <p>Lorem ipsum dolor sit amet, consectetuer adipiscing elit.<br>Aenean commodo ligula eget dolor aenean massa.<br>Cum sociis natoque penatibus .</p>
    <div class="pay">Tillbee</div>
  </div>
  <div class="abs fcol" style="left:488px">
    <h4>Useful Links</h4>
    <ul><li>About us</li><li>Services</li><li>Search</li><li>Orders and Payments</li><li>Contact</li></ul>
  </div>
  <div class="abs fcol" style="left:720px">
    <h4>My Account</h4>
    <ul><li>Log In</li><li>View Pricing</li><li>My wish list</li><li>Order</li><li>sHelp</li></ul>
  </div>
  <div class="abs fcol follow" style="left:940px">
    <h4 style="margin-bottom:9px">Follow us</h4>
    <ul><li><i></i>Facepage</li><li class="hot"><i></i>Chirper</li><li><i></i>Searchly +</li><li><i></i>Snapgram</li></ul>
  </div>
  <div class="abs bottombar">
    <span class="abs copy">© Brightpeak Roofing</span>
    <div class="abs legal"><span>Privacy Policy</span><span>|</span><span>Terms &amp; Conditions</span></div>
  </div>
</footer>

</body>
</html>
```